Business Card Design

Marla Quenby
Artist of Contemporary/Modern/Representational Art
Contact: 0429175348
Please include my web site (thanks)! http://www.artloft583.com.au/marla-quenby
And
Email: marlaquenby@vexmail.com

Target Market(s)

Modern professional People who know what they like in modern contemporary art and have the means to purchase it.

Industry/Entity Type

Business

Contact Information for Business Card

Marla Quenby
Contact: 0429175348

Font styles to use
Sans Serif

Requirements
Must have
• Simplicity & to the point
Keep the font modern/ contemporary
Nice to have
• A portrait of me and one piece of work on the business card (one on each side).
Should not have
• I'm not into butterflies.
No feminine style swirls
Nor I like swirls that look like tatoos

```html
<!DOCTYPE html>
<html lang="en">
<head>
<meta charset="utf-8">
<title>Marla Quenby – Business Card</title>
<link rel="stylesheet" href="https://fonts.googleapis.com/css2?family=Open+Sans:wght@700&family=Arimo:wght@400&display=swap">
<style>
  :root {
    --page: #ffffff;
    --card: #000000;
    --name-red: #c5344f;
    --gold: #c49a3a;
    --gold-dark: #7a5b1c;
    --white: #ffffff;
    --grey-glow: #4a4a4a;
    --ring-yellow: #f4ee1a;
    --ring-purple: #9b3ff0;
    --ring-magenta: #ee2ad8;
    --ring-green: #6cf22a;
    --ring-peach: #e6c2a8;
  }
  * { box-sizing: border-box; margin: 0; padding: 0; }
  html, body { width: 1200px; height: 416px; overflow: hidden; background: var(--page); }
  .canvas { position: relative; width: 1200px; height: 416px; }

  .card { position: absolute; top: 0; background: var(--card); overflow: hidden; }
  .card--front { left: 8px; width: 589px; height: 400px; }
  .card--back {
    left: 605px; width: 590px; height: 398px;
    background: radial-gradient(ellipse 60% 70% at 50% 55%, var(--grey-glow) 0%, #1c1c1c 55%, #000 100%);
  }

  .front__name {
    position: absolute; left: 37px; top: 48px;
    font-family: "Open Sans", sans-serif; font-weight: 700;
    font-size: 38px; color: var(--name-red); letter-spacing: 0.5px;
  }
  .front__splash {
    position: absolute; left: 55px; top: 125px; width: 215px; height: 215px;
    background: radial-gradient(circle at 45% 45%, var(--gold) 0%, var(--gold-dark) 45%, rgba(0,0,0,0) 72%);
  }
  .front__mark {
    position: absolute; left: 130px; top: 282px;
    font-family: "Open Sans", sans-serif; font-weight: 700;
    font-size: 15px; color: var(--gold);
  }
  .artwork { position: absolute; left: 329px; width: 254px; }
  .artwork--street {
    top: 13px; height: 188px;
    background: linear-gradient(160deg, #d8b33a 0%, #b8c27a 35%, #e04a8a 55%, #cfd6dc 80%, #8a9aa0 100%);
  }
  .artwork--town {
    top: 207px; height: 185px;
    background: linear-gradient(180deg, #9fc5c8 0%, #c8553a 35%, #d88a3a 60%, #2f7a86 85%, #aacfd0 100%);
  }

  .back__rings { position: absolute; inset: 0; width: 590px; height: 398px; }
  .back__rings circle { fill: none; stroke-width: 5; }
  .back__content {
    position: absolute; left: 0; right: 0; top: 50px; text-align: center; color: var(--white);
    font-family: "Arimo", sans-serif; font-size: 17px;
  }
  .back__name {
    font-family: "Open Sans", sans-serif; font-weight: 700;
    font-size: 38px; letter-spacing: 0.5px; margin-bottom: 32px; padding-left: 8px;
  }
  .back__line { line-height: 1; margin-bottom: 27px; word-spacing: 2px; }
</style>
</head>
<body>
<main class="canvas">
  <section class="card card--front">
    <h1 class="front__name">Marla Quenby</h1>
    <div class="front__splash" role="img" aria-label="Gold paint splash motif"></div>
    <span class="front__mark">Marla Quenby</span>
    <div class="artwork artwork--street" role="img" aria-label="Painting of a street with a pink house and bare trees"></div>
    <div class="artwork artwork--town" role="img" aria-label="Painting of an old town on an island seen from above"></div>
  </section>

  <section class="card card--back">
    <svg class="back__rings" viewBox="0 0 590 398" aria-hidden="true">
      <circle cx="60" cy="58" r="36" stroke="var(--ring-yellow)"/>
      <circle cx="94" cy="51" r="38" stroke="var(--ring-purple)"/>
      <circle cx="506" cy="72" r="34" stroke="var(--ring-magenta)"/>
      <circle cx="553" cy="99" r="33" stroke="var(--ring-yellow)"/>
      <circle cx="91" cy="223" r="33" stroke="var(--ring-green)"/>
      <circle cx="55" cy="270" r="33" stroke="var(--ring-magenta)"/>
      <circle cx="61" cy="323" r="33" stroke="var(--ring-peach)"/>
      <circle cx="540" cy="254" r="32" stroke="var(--ring-green)"/>
      <circle cx="465" cy="334" r="33" stroke="var(--ring-peach)"/>
      <circle cx="535" cy="322" r="36" stroke="var(--ring-purple)"/>
    </svg>
    <div class="back__content">
      <h2 class="back__name">Marla Quenby</h2>
      <p class="back__line">Artist of contemporary/Modern/Representational art</p>
      <p class="back__line">Contact: 0429175348</p>
      <p class="back__line">www.artloft583.com.au/marla-quenby</p>
      <p class="back__line">marlaquenby@vexmail.com</p>
    </div>
  </section>
</main>
</body>
</html>
```